Inspiring Poster for Company Staff Room

What we need:
We want an awesome design to create a poster that will be plaque mounted in our staff room. We just went through a very motivating workshop to discover our "WHY" as a company...basically, to define the reason we are in business, and to define what motivates us to come to work every day. The poster must be motivating but really resonate with our team…we are not looking for a “typical” motivational poster that we can purchase off Brindleway!

Who we are:
We are a property management company, a team of 20 that is passionate about our investors, and residents who rent from us, but more importantly, we love helping people and making a difference in our industry. We are proud and work hard for every single 5 star Quorvix review we achieve.

Information for you:
We have included a mock up of the poster, which words we want, and the placement of them (in a general sense) but we need a designer to really bring this together in an inspiring poster that represents our company’s culture, feel, and fit. We have also included a logo file, as well as examples of our business cards, letterhead and thank you card already designed.
Here are the parameters:

(1) Poster size: 24” x 36”
(2) Full colour
(3) Must incorporate our company logo
(4) Must incorporate the following words:

Why do I come to work?

“To feel fulfilled by empathizing, educating and empowering our clients and co-workers so that we can build strong, impactful relationships”

Own the outcome

(5) Please see our website at www.larkmoorpm.example to get a feel for our company culture and for a better idea of our current company graphics

Target Market(s)

Our staff. Will not be seen by our clients

Industry/Entity Type

Real Estate

Font styles to use
Serif
Sans Serif

Requirements
Should not have
• Would not want this to be too "busy." if you can picture it, the poster will be mounted on the wall as soon as someone enters the room. The idea is to remind them each day why they come to work.

```html
<!DOCTYPE html>
<html lang="en">
<head>
<meta charset="utf-8">
<title>Why do I come to work? – Larkmoor Property Management</title>
<link rel="stylesheet" href="https://fonts.googleapis.com/css2?family=Abril+Fatface&family=Poppins:wght@300;600&display=swap">
<style>
  :root {
    --brand-blue: #1794cf;
    --brand-charcoal: #404141;
    --ink: #333435;
    --paper: #ffffff;
    --skyline: #f3f4f6;
  }
  html, body {
    margin: 0;
    padding: 0;
    overflow: hidden;
    background: var(--paper);
  }
  .poster {
    position: relative;
    width: 800px;
    height: 1200px;
    overflow: hidden;
    background: var(--paper);
    font-family: "Poppins", sans-serif;
    color: var(--ink);
  }
  .corner-shapes {
    position: absolute;
    inset: 0;
    width: 800px;
    height: 1200px;
  }
  .skyline {
    position: absolute;
    left: 0;
    top: 900px;
    width: 800px;
    height: 300px;
    background: linear-gradient(to bottom, rgba(243,244,246,0) 0%, var(--skyline) 40%, var(--skyline) 100%);
  }
  .brand {
    position: absolute;
    left: 425px;
    top: 64px;
    display: flex;
    align-items: center;
    gap: 14px;
  }
  .brand-mark {
    width: 46px;
    height: 46px;
    background: var(--brand-charcoal);
  }
  .brand-name {
    font-family: "Poppins", sans-serif;
    font-weight: 600;
    color: var(--brand-blue);
    line-height: 1.05;
    letter-spacing: 2px;
  }
  .brand-name .word { display: block; font-size: 28px; letter-spacing: 4px; }
  .brand-name .sub { display: block; font-size: 11px; letter-spacing: 3px; }
  .headline-why {
    position: absolute;
    left: 68px;
    top: 120px;
    margin: 0;
    font-family: "Abril Fatface", serif;
    font-weight: 400;
    font-size: 152px;
    line-height: 1;
    color: var(--brand-charcoal);
    letter-spacing: -4px;
  }
  .headline-question {
    position: absolute;
    top: 262px;
    margin: 0;
    font-family: "Abril Fatface", serif;
    font-size: 56px;
    line-height: 1;
    color: var(--brand-blue);
    letter-spacing: -1px;
    word-spacing: 2px;
  }
  .headline-question.lead { left: 74px; }
  .headline-question.tail { left: 368px; }
  .purpose {
    position: absolute;
    left: 70px;
    top: 0;
    margin: 0;
  }
  .purpose .line {
    position: absolute;
    left: 0;
    white-space: nowrap;
    font-weight: 300;
    font-size: 46px;
    letter-spacing: -2px;
    line-height: 1;
  }
  .purpose .strong {
    font-weight: 600;
    font-size: 66px;
    letter-spacing: -2.5px;
    position: relative;
    z-index: 1;
  }
  .underline {
    position: absolute;
    height: 11px;
    background: var(--brand-blue);
  }
  .underline.first { left: 65px; top: 456px; width: 521px; }
  .underline.second { left: 281px; top: 899px; width: 428px; height: 12px; }
  .motto {
    position: absolute;
    left: 69px;
    top: 985px;
    margin: 0;
    font-family: "Abril Fatface", serif;
    font-weight: 400;
    font-size: 62px;
    line-height: 1;
    color: var(--brand-blue);
    letter-spacing: -0.5px;
  }
</style>
</head>
<body>
<main class="poster">
  <div class="skyline" role="img" aria-label="Faint city skyline with a cable bridge and towers"></div>

  <svg class="corner-shapes" viewBox="0 0 800 1200" aria-hidden="true">
    <polygon class="top-dark" points="0,0 223,0 223,100" fill="var(--brand-charcoal)"/>
    <polygon class="top-blue" points="223,0 800,0 800,14 414,14 223,100" fill="var(--brand-blue)"/>
    <polygon class="bottom-dark" points="0,1185 380,1185 571,1099 571,1200 0,1200" fill="var(--brand-charcoal)"/>
    <polygon class="bottom-blue" points="571,1099 790,1200 571,1200" fill="var(--brand-blue)"/>
  </svg>

  <div class="brand">
    <div class="brand-mark"></div>
    <div class="brand-name">
      <span class="word">LARKMOOR</span>
      <span class="sub">PROPERTY MANAGEMENT</span>
    </div>
  </div>

  <h1 class="headline-why">Why</h1>
  <p class="headline-question lead">do I come</p>
  <p class="headline-question tail">to work?</p>

  <div class="underline first"></div>
  <div class="underline second"></div>

  <blockquote class="purpose">
    <span class="line" style="top:410px">To <span class="strong">feel fulfilled</span> by</span>
    <span class="line" style="top:500px">empathizing,</span>
    <span class="line" style="top:574px">educating</span>
    <span class="line" style="top:648px">and empowering our</span>
    <span class="line" style="top:722px">clients and co-workers</span>
    <span class="line" style="top:796px">so that we can build strong,</span>
    <span class="line" style="top:852px">impactful <span class="strong">relationships</span></span>
  </blockquote>

  <p class="motto">Own the Outcome</p>
</main>
</body>
</html>
```